General Dental Office Business Card

I run a private general dental office in southern California, and would like a refresh/redesign of my business card. I focus on quality care rather than volume. The email address on the uploaded current card should be updated to: info@marbleshoredental.example. The current card's logo is a deboss, but I am open to other ideas. The logo can be refreshed, but it is something that's been with me since the beginning of the office, so I wouldn't want a drastic redesign.
Target Market(s)
Adults 18-99, whoever needs dental services
Industry/Entity Type
Healthcare/Dental
Contact Information for Business Card
Name, Address, Phone, email
Colors
Designer to choose colors to be used in the design.
Requirements
Must have
- Logo (Same as original one in the uploaded file), space on back for appointment time/date

```html
<!DOCTYPE html>
<html lang="en">
<head>
<meta charset="utf-8">
<title>Marble Shore Dental – Business Card</title>
<link href="https://fonts.googleapis.com/css2?family=Montserrat:wght@400;500&display=swap" rel="stylesheet">
<style>
  :root {
    --backdrop: #3a3a3c;
    --card-white: #ffffff;
    --card-black: #1c1c1d;
    --sky: #86d6ec;
    --navy: #141b26;
    --ink: #1a1a1a;
    --dots: #555555;
  }
  * { margin: 0; padding: 0; box-sizing: border-box; }
  html, body { width: 1200px; height: 1200px; overflow: hidden; }
  body {
    background: var(--backdrop);
    font-family: "Montserrat", sans-serif;
    position: relative;
  }
  .card {
    position: absolute;
    left: 220px;
    width: 760px;
    height: 434px;
    border-radius: 30px;
    overflow: hidden;
  }
  .card-front { top: 110px; background: var(--card-white); }
  .card-back  { top: 620px; background: var(--card-black); }

  .front-band { position: absolute; left: 0; bottom: 0; width: 760px; height: 434px; }

  .identity { position: absolute; left: 52px; top: 150px; }
  .doctor-name {
    color: var(--sky); font-size: 34px; font-weight: 400; letter-spacing: 0.5px; line-height: 1;
  }
  .specialty { color: var(--ink); font-size: 24px; margin-top: 4px; }

  .contact-list { position: absolute; left: 52px; top: 232px; list-style: none; }
  .contact-list li {
    display: flex; align-items: flex-start; gap: 14px;
    color: var(--ink); font-size: 19px; line-height: 1.25; margin-bottom: 4px;
  }
  .contact-list svg { width: 22px; height: 22px; flex: none; margin-top: 1px; fill: var(--sky); }

  .brand-front {
    position: absolute; right: 48px; top: 48px;
    display: flex; flex-direction: column; align-items: center; gap: 14px;
  }
  .brand-dot { width: 150px; height: 150px; border-radius: 50%; background: var(--sky); }
  .brand-name-front { color: var(--sky); font-size: 18px; font-weight: 500; }

  .appointment { position: absolute; left: 96px; top: 312px; font-size: 17px; color: var(--ink); }
  .appointment .field { display: flex; align-items: baseline; gap: 6px; }
  .appointment .line { border-bottom: 2px dotted var(--dots); height: 1px; }
  .field-date { position: absolute; left: 0; top: 40px; }
  .field-date .line { width: 230px; }
  .field-time { position: absolute; left: 300px; top: 0; }
  .field-time .line { width: 250px; }

  .website {
    position: absolute; right: 40px; bottom: 22px;
    color: var(--card-white); font-size: 17px; letter-spacing: 0.3px;
  }

  .brand-back {
    position: absolute; inset: 0;
    display: flex; flex-direction: column; align-items: center; justify-content: center; gap: 26px;
  }
  .brand-back .brand-dot { width: 170px; height: 170px; }
  .brand-name-back { color: var(--card-white); font-size: 44px; font-weight: 500; }
</style>
</head>
<body>

  <section class="card card-front">
    <svg class="front-band" viewBox="0 0 760 434" aria-hidden="true">
      <path d="M0 408 L420 378 C470 374 480 350 520 340 L760 318 L760 434 L0 434 Z" fill="var(--sky)"/>
      <path d="M0 420 L440 384 C500 378 500 340 560 334 L760 316 L760 434 L0 434 Z" fill="var(--navy)"/>
    </svg>

    <div class="identity">
      <h1 class="doctor-name">ELENA R. VOSS DDS</h1>
      <p class="specialty">General Dentistry</p>
    </div>

    <ul class="contact-list">
      <li>
        <svg viewBox="0 0 24 24"><path d="M6.6 10.8a15 15 0 0 0 6.6 6.6l2.2-2.2c.3-.3.7-.4 1-.2 1.1.4 2.3.6 3.6.6.6 0 1 .4 1 1V20c0 .6-.4 1-1 1C10.6 21 3 13.4 3 4c0-.6.4-1 1-1h3.5c.6 0 1 .4 1 1 0 1.3.2 2.5.6 3.6.1.3 0 .7-.2 1z"/></svg>
        555-014-2290
      </li>
      <li>
        <svg viewBox="0 0 24 24"><path d="M2 5h20v14H2z M3.5 6.5 12 13l8.5-6.5" stroke="var(--card-white)" stroke-width="1.5"/></svg>
        info@marbleshoredental.example
      </li>
      <li>
        <svg viewBox="0 0 24 24"><path d="M12 2a7 7 0 0 0-7 7c0 5 7 13 7 13s7-8 7-13a7 7 0 0 0-7-7zm0 9.5A2.5 2.5 0 1 1 12 6.5a2.5 2.5 0 0 1 0 5z"/></svg>
        <span>210 Harbor View Lane<br>Seaside, CA 90000</span>
      </li>
    </ul>

    <div class="brand-front">
      <div class="brand-dot"></div>
      <span class="brand-name-front">Marble Shore Dental</span>
    </div>

    <div class="appointment">
      <div class="field field-time"><span>Time:</span><span class="line"></span></div>
      <div class="field field-date"><span>Date:</span><span class="line"></span></div>
    </div>

    <p class="website">www.marbleshoredental.example</p>
  </section>

  <section class="card card-back">
    <div class="brand-back">
      <div class="brand-dot"></div>
      <span class="brand-name-back">Marble Shore Dental</span>
    </div>
  </section>

</body>
</html>
```